Buch-/E-Book-Cover für Selfpublisher
Zielgruppe
Ich bin ein Selfpublisher. Meine Zielgruppe sind Menschen ab dem mittleren Alter.
Aufgabenstellung
Das Cover sollte nicht verspielt sein, sondern klar und nüchtern.
Es muss in Briefmarkengröße ebenso wirken wie im Mittel- und Großformat.

```html
<!DOCTYPE html>
<html lang="de">
<head>
<meta charset="utf-8">
<title>Spuren im Lammfell – Buchumschlag</title>
<link rel="stylesheet" href="https://fonts.googleapis.com/css2?family=Arimo:wght@700&family=Roboto+Condensed:wght@700&family=Nunito+Sans:wght@800&display=swap">
<style>
  :root {
    --rose: #f9dcdd;
    --lilac: #b3b0c6;
    --sky: #c8dbe4;
    --white: #ffffff;
    --paper: #d3cab6;
    --frame-red: #c8242f;
    --author-brown: #5c3516;
    --ink: #1f1f1f;
    --blurb-blue: #2a4a9a;
    --frame-black: #000000;
    --frame-grey: #6a6870;
  }
  * { margin: 0; padding: 0; box-sizing: border-box; }
  html, body { width: 1200px; height: 751px; overflow: hidden; background: var(--white); }
  .cover { position: relative; width: 1200px; height: 751px; }
  .pattern {
    position: absolute; top: 0; height: 751px;
    background: linear-gradient(160deg, var(--rose) 0%, var(--lilac) 30%, var(--rose) 50%, var(--sky) 70%, var(--lilac) 100%);
  }
  .pattern--back { left: 0; width: 557px; }
  .pattern--front { left: 646px; width: 554px; }
  .spine { position: absolute; left: 557px; top: 0; width: 89px; height: 751px; background: var(--white); }
  .spine-text {
    position: absolute; left: 44px; transform-origin: 0 0; transform: rotate(90deg) translateY(-50%);
    font-family: "Arimo", Arial, sans-serif; font-weight: 700; font-size: 28px; line-height: 1;
    color: var(--ink); white-space: nowrap; letter-spacing: 0.5px;
  }
  .spine-title { top: 18px; }
  .spine-author { top: 508px; }
  .shapes { position: absolute; inset: 0; }
  .author {
    position: absolute; left: 646px; width: 554px; top: 30px; text-align: center;
    font-family: "Arimo", Arial, sans-serif; font-weight: 700; font-size: 62px; letter-spacing: 1px;
    color: var(--author-brown); line-height: 1;
  }
  .title {
    position: absolute; left: 728px; width: 387px; text-align: center;
    font-family: "Roboto Condensed", "Arial Narrow", sans-serif; font-weight: 700;
    color: var(--ink); line-height: 1; font-size: 56px;
  }
  .title .cap { font-size: 78px; }
  .title-1 { top: 238px; }
  .title-2 { top: 342px; font-size: 54px; }
  .title-3 { top: 412px; }
  .genre {
    position: absolute; left: 646px; width: 574px; top: 692px; text-align: center;
    font-family: "Arimo", Arial, sans-serif; font-weight: 700; font-size: 30px; letter-spacing: 1.5px;
    color: var(--ink); line-height: 1;
  }
  .blurb {
    position: absolute; left: 68px; top: 278px; width: 460px;
    font-family: "Nunito Sans", Verdana, sans-serif; font-weight: 800; font-size: 22px; line-height: 26.3px;
    color: var(--blurb-blue); white-space: pre;
  }
</style>
</head>
<body>
<div class="cover">
  <div class="pattern pattern--back" role="img" aria-label="Abstraktes Wellenmuster in Rosa, Flieder und Hellblau"></div>
  <div class="pattern pattern--front" role="img" aria-label="Abstraktes Wellenmuster in Rosa, Flieder und Hellblau"></div>
  <div class="spine">
    <div class="spine-text spine-title">SPUREN IM LAMMFELL</div>
    <div class="spine-text spine-author">KONRAD WELS</div>
  </div>

  <svg class="shapes" width="1200" height="751" viewBox="0 0 1200 751" aria-hidden="true">
    <g class="blurb-box">
      <rect x="36" y="222" width="484" height="312" fill="#ffffff" fill-opacity="0.55" stroke="var(--frame-grey)" stroke-width="2"/>
      <path d="M91 211 H532 V484 A67 67 0 0 0 472 545 H24 V278 A67 67 0 0 0 91 211 Z" fill="none" stroke="var(--frame-black)" stroke-width="2.5"/>
    </g>
    <rect class="title-panel" x="728" y="112" width="387" height="525" fill="var(--paper)"/>
    <rect class="title-frame" x="738" y="157" width="366" height="448" fill="none" stroke="var(--frame-red)" stroke-width="3.5"/>
  </svg>

  <div class="author">KONRAD WELS</div>
  <div class="title title-1"><span class="cap">S</span>PUREN</div>
  <div class="title title-2">IM</div>
  <div class="title title-3"><span class="cap">L</span>AMMFELL</div>
  <div class="genre">ERZÄHLUNGEN</div>

  <p class="blurb">In der titelgebenden Erzählung steht ein
 Arzt vor Gericht Ihm wird vorgeworfen,
einen Patienten durch eine bewusst
falsche Diagnose in den Tod getrieben
zu haben.
Der Arzt beteuert seine Unschuld, aber
 allmählich kommt das wahre Gesicht
des Angeklagten zum Vorschein........</p>
</div>
</body>
</html>
```